Plakat-Design für eine Ranch mit Gastronomie
Zielgruppe
Ranch und Gastronomie
Aufgabenstellung
Werbebanner 240 cm x 120 cm
Daten:
Url: http://www.talmuehle-hof.de
http://www.birkental-ranch.de
Plaudernetz Button
Text-Ranch:
Reittuntericht & Kurse
Kutschfahrten
Ausritte
Beritt
Pferdepension
Deckhengste
Reitbeteiligungen
Text-Saloon/Gastronomie:
Feiern
Tagungen
Hochzeiten
Erlebnissgastronomie

```html
<!DOCTYPE html>
<html lang="de">
<head>
<meta charset="utf-8">
<title>Talmühle-Hof – Ranch &amp; Saloon</title>
<link href="https://fonts.googleapis.com/css2?family=Rye&family=Lora:ital,wght@0,400;0,600;1,400&display=swap" rel="stylesheet">
<style>
:root{
  --stage:#2a2d33;
  --wood-dark:#6a3e1c;
  --wood-mid:#8f5a2b;
  --wood-light:#b27c42;
  --band:#d09354;
  --ink:#2b1a0e;
  --gold:#e8d27a;
  --paper:#f3f1ec;
  --paper-shade:#dedad2;
  --text:#1e1e1e;
  --frame:#ffffff;
}
*{margin:0;padding:0;box-sizing:border-box}
html,body{width:1200px;height:782px;overflow:hidden;background:var(--stage)}
.banner{
  position:absolute;left:20px;top:101px;width:1160px;height:580px;overflow:hidden;
  font-family:"Lora",Georgia,serif;color:var(--text);
}
.backdrop{
  position:absolute;inset:0;
  background:linear-gradient(90deg,var(--wood-mid),var(--wood-light) 22%,var(--wood-mid) 42%,var(--wood-dark) 55%,var(--wood-light) 78%,var(--wood-mid));
}
.photo{position:absolute;border:5px solid var(--frame);box-shadow:2px 4px 8px rgba(0,0,0,.45);z-index:4}
.photo-castle{left:23px;top:128px;width:209px;height:174px;transform:rotate(-3deg);background:linear-gradient(#e9b39a,#7d8aa6 45%,#3c4a66 70%,#2b2f3c)}
.photo-barn{left:800px;top:40px;width:336px;height:192px;transform:rotate(-3deg);background:linear-gradient(#4f7fc4,#d8e2ee 35%,#3a3a3c 60%,#6b6b66)}
.photo-crowd{left:93px;top:486px;width:120px;height:78px;transform:rotate(-2deg);background:linear-gradient(#c7d3df,#6b6f7a 50%,#3f4a5c)}
.photo-meadow{left:208px;top:502px;width:124px;height:80px;transform:rotate(-3deg);background:linear-gradient(#d8e6ee,#4b7a36 45%,#6fa048)}
.photo-interior{left:700px;top:308px;width:130px;height:72px;transform:rotate(-2deg);background:linear-gradient(135deg,#5b3a22,#c79a62 50%,#3d2616)}
.brand{position:absolute;left:250px;top:110px;width:520px;display:flex;align-items:center;justify-content:center;gap:18px;transform:rotate(-3deg);z-index:2}
.brand-mark{width:92px;height:92px;border-radius:50%;background:var(--gold)}
.brand-name{font-family:"Lora",Georgia,serif;font-weight:600;font-size:42px;color:var(--gold);letter-spacing:1px}
.sign{
  position:absolute;display:flex;align-items:center;justify-content:center;
  background:var(--band);z-index:3;
  font-family:"Rye",serif;color:var(--ink);letter-spacing:1px;line-height:1;
}
.sign-ranch{left:35px;top:278px;width:430px;height:66px;transform:rotate(-2deg);font-size:38px}
.sign-saloon{left:520px;top:232px;width:560px;height:72px;transform:rotate(-2deg);font-size:44px}
.paper{position:absolute;background:linear-gradient(160deg,var(--paper),var(--paper-shade));z-index:1}
.paper-ranch{left:38px;top:330px;width:436px;height:215px}
.paper-saloon{left:512px;top:290px;width:576px;height:262px}
.list{position:absolute;list-style:none;font-style:italic;font-size:21px;line-height:1.24;z-index:2;white-space:nowrap}
.list li::before{content:"• ";font-size:15px;vertical-align:middle}
.list-ranch-a{left:52px;top:364px}
.list-ranch-b{left:262px;top:356px}
.list-saloon{left:530px;top:350px;font-size:24px;line-height:1.28}
.contact{position:absolute;right:100px;top:326px;text-align:right;font-style:italic;font-size:16px;line-height:1.32;z-index:2;white-space:nowrap}
.contact .address{margin-bottom:18px}
.contact .plain{font-style:normal}
</style>
</head>
<body>
<main class="banner">
  <div class="backdrop" role="img" aria-label="Wand aus rustikalen Holzbrettern"></div>

  <div class="photo photo-castle" role="img" aria-label="Burg auf einem Hügel in der Abenddämmerung, Reiter im Vordergrund"></div>

  <div class="brand">
    <span class="brand-mark"></span>
    <span class="brand-name">Talmühle-Hof</span>
  </div>

  <div class="photo photo-barn" role="img" aria-label="Pferdekutsche vor einer großen Scheune unter blauem Himmel"></div>

  <div class="paper paper-ranch"></div>
  <div class="sign sign-ranch">RANCH</div>
  <ul class="list list-ranch-a">
    <li>Reittuntericht<br>&nbsp;&nbsp;&amp; Kurse</li>
    <li>Kutschfahrten</li>
    <li>Ausritte</li>
  </ul>
  <ul class="list list-ranch-b">
    <li>Beritt</li>
    <li>Pferdepension</li>
    <li>Deckhengste</li>
    <li>Reitbeteiligungen</li>
  </ul>
  <div class="photo photo-crowd" role="img" aria-label="Besuchergruppe bei einer Veranstaltung auf der Ranch"></div>
  <div class="photo photo-meadow" role="img" aria-label="Pferde und Hund auf einer grünen Weide"></div>

  <div class="paper paper-saloon"></div>
  <div class="sign sign-saloon">SALOON</div>
  <div class="photo photo-interior" role="img" aria-label="Gastraum des Saloons mit Holzeinrichtung"></div>
  <ul class="list list-saloon">
    <li>Feiern</li>
    <li>Tagungen</li>
    <li>Hochzeiten</li>
    <li>Erlebnis<br>&nbsp;&nbsp;Gastronomie</li>
  </ul>
  <address class="contact">
    <div class="address">Talmühle-Hof &amp;<br>Birkental Ranch<br>Lindenweg 12<br><span class="plain">98670 Birkenau</span></div>
    <div><span class="plain">Tel: 036 555 / 120 40<br>Mobil: 0151 / 555 123 45</span><br>info@talmuehle-hof.de<br>www.talmuehle-hof.de</div>
  </address>
</main>
</body>
</html>
```